New Business Card Design Project

I would like my card design to look exactly like the logo, design, layout, and print of the current attached file. The only change I would like made would be for the print to say THE KMR GROUP instead of THE MORALES GROUP. Basically, just replace his group name with my group name. I would also like the backgroud to be the same texture and color as the attached file. I love the dark blue lettering and house logo on the card.

I am completely open to the rest of the card design. I just want something clean and simple. Only basic contact info required on the card. Maybe just name: Wade K Holmer and cell # 555.014.2289 and email wade@thepxbroker.com

```html
<!DOCTYPE html>
<html lang="en">
<head>
<meta charset="utf-8">
<title>Wade K Holmer — Business Card</title>
<link rel="stylesheet" href="https://fonts.googleapis.com/css2?family=Lato:wght@400&display=swap">
<style>
  :root {
    --page: #ffffff;
    --paper: #f4f4f2;
    --paper-shade: #efefec;
    --navy: #22265a;
    --ink: #1b1b24;
  }
  html, body {
    margin: 0;
    padding: 0;
    width: 1200px;
    height: 1200px;
    overflow: hidden;
    background: var(--page);
    font-family: "Lato", sans-serif;
  }
  .card {
    position: absolute;
    left: 40px;
    top: 249px;
    width: 1120px;
    height: 703px;
    background: linear-gradient(135deg, var(--paper) 0%, var(--paper-shade) 50%, var(--paper) 100%);
  }
  .brand-square {
    position: absolute;
    left: 65px;
    top: 84px;
    width: 102px;
    height: 102px;
    background: var(--navy);
  }
  .brand-divider {
    position: absolute;
    left: 195px;
    top: 76px;
    width: 2px;
    height: 127px;
    background: var(--navy);
  }
  .brand-name {
    position: absolute;
    left: 210px;
    top: 94px;
    margin: 0;
    font-size: 34px;
    line-height: 30px;
    font-weight: 400;
    letter-spacing: 2px;
    color: var(--navy);
  }
  .brand-name span { display: block; }
  .person-name {
    position: absolute;
    left: 334px;
    top: 276px;
    margin: 0;
    font-size: 72px;
    line-height: 1;
    font-weight: 400;
    color: var(--navy);
  }
  .contact {
    position: absolute;
    left: 334px;
    margin: 0;
    font-size: 34px;
    line-height: 1;
    color: var(--navy);
  }
  .contact-cell { top: 389px; }
  .contact-mail { top: 458px; }
  .contact-label {
    display: inline-block;
    width: 85px;
    color: var(--ink);
  }
</style>
</head>
<body>
  <div class="card">
    <div class="brand-square"></div>
    <div class="brand-divider"></div>
    <h2 class="brand-name"><span>THE</span><span>KMR</span><span>GROUP</span></h2>

    <h1 class="person-name">Wade K Holmer</h1>
    <p class="contact contact-cell"><span class="contact-label">Cell</span>555.014.2289</p>
    <p class="contact contact-mail"><span class="contact-label">Mail</span>wade@thepxbroker.com</p>
  </div>
</body>
</html>
```